Web Page Flash Animation Needed

We are looking for a Flash animation element for our website Home page. Essentially what we are envisioning is using the attached photo of a painting to create a "jigsaw puzzle" which comes together (animation) to display the painting, with each piece of the puzzle being a link to each page of our site. Attached you will also see a sketch of sort of how we envision this looking, along with a list of the individual pages of our website.

We are thinking that the size of the Flash element should be so that it fits on a single screen (no scrolling) of most modern monitors. We're looking for a lot of creativity - so if you have a better way of doing this - even if it's not Flash - we are open to alternative ideas.

*I have included a copy of our logo - I believe what we envision is 8 puzzle pieces: 7 for each of the site pages and the other for our logo. The pieces come in and together as the page loads. Again, open to alternate ideas & creativity.

Please reach out to me with any questions regarding the project.

Industry/Entity Type

Painting

```html
<!DOCTYPE html>
<html lang="en">
<head>
<meta charset="utf-8">
<title>Crestline Group – Puzzle Home Animation</title>
<link rel="stylesheet" href="https://fonts.googleapis.com/css2?family=PT+Sans:wght@400;700&display=swap">
<style>
  :root {
    --stage-bg: #ececec;
    --frame-border: #1f4f7a;
    --frame-bg: #ffffff;
    --brand-teal: #0b5a6b;
    --headline-green: #0d6b52;
    --tile-blue: #cfe0ea;
    --tile-mint: #e4f0ee;
    --button-navy: #12386e;
    --note-grey: #444444;
    --paint-dark: #2a0d08;
    --paint-red: #8a1e12;
    --paint-gold: #e8c25a;
  }
  * { box-sizing: border-box; margin: 0; padding: 0; }
  html, body { width: 1200px; height: 1000px; overflow: hidden; }
  body {
    position: relative;
    background:
      repeating-linear-gradient(45deg, rgba(0,0,0,0.025) 0 2px, transparent 2px 4px),
      radial-gradient(ellipse at center, #fafafa 0%, var(--stage-bg) 100%);
    font-family: "PT Sans", Arial, sans-serif;
  }
  .frame {
    position: absolute;
    width: 398px; height: 311px;
    background: var(--frame-bg);
    border: 1px solid var(--frame-border);
  }
  .frame--intro   { left: 20px;  top: 15px; }
  .frame--assemble{ left: 790px; top: 15px; }
  .frame--complete{ left: 407px; top: 350px; }
  .frame--clients { left: 8px;   top: 676px; height: 312px; }
  .frame--team    { left: 790px; top: 676px; height: 312px; }

  .brand {
    position: absolute;
    left: 8px; width: 232px;
    text-align: center;
    font-size: 25px;
    font-weight: 400;
    letter-spacing: 0.5px;
    color: var(--brand-teal);
    white-space: nowrap;
  }
  .brand--solo { top: 103px; }
  .brand--top  { top: 89px; }

  .headline {
    position: absolute;
    left: 8px; width: 232px; top: 140px;
    text-align: center;
    font-size: 24px;
    font-weight: 700;
    line-height: 32px;
    color: var(--headline-green);
  }

  .board {
    position: absolute;
    right: 7px; top: 7px;
    width: 148px; height: 296px;
  }
  .board svg { display: block; }

  .loose-piece {
    position: absolute;
    background: linear-gradient(135deg, var(--paint-red), var(--paint-dark));
  }
  .loose-piece--intro { left: 142px; top: 236px; width: 48px; height: 62px; }
  .loose-piece--flying {
    left: 236px; top: 190px; width: 70px; height: 74px;
    transform: rotate(-22deg);
    background: linear-gradient(135deg, var(--paint-gold), var(--paint-red) 60%, var(--paint-dark));
  }

  .note {
    position: absolute;
    font-size: 14px;
    color: var(--note-grey);
    text-align: center;
    width: 360px;
  }
  .note--animation { left: 425px; top: 144px; }
  .note--buttons   { left: 422px; top: 823px; }

  .button-label {
    font-family: "PT Sans", Arial, sans-serif;
    font-size: 10px;
    fill: #ffffff;
  }
</style>
</head>
<body>

<svg width="0" height="0" style="position:absolute">
  <defs>
    <linearGradient id="painting" x1="0" y1="0" x2="0" y2="1">
      <stop offset="0" stop-color="#7a1a10"/>
      <stop offset="0.3" stop-color="#c8782e"/>
      <stop offset="0.55" stop-color="#e8c25a"/>
      <stop offset="0.75" stop-color="#5a2a14"/>
      <stop offset="1" stop-color="#1f0a06"/>
    </linearGradient>
  </defs>
</svg>

<!-- Step 1: empty board, first piece arrives -->
<section class="frame frame--intro">
  <div class="brand brand--solo">CRESTLINE GROUP</div>
  <div class="board">
    <svg width="148" height="296" viewBox="0 0 148 296">
      <rect x="0" y="0" width="74" height="74" fill="var(--tile-blue)"/>
      <rect x="74" y="0" width="74" height="74" fill="var(--tile-mint)"/>
      <rect x="0" y="74" width="74" height="74" fill="var(--tile-mint)"/>
      <rect x="74" y="74" width="74" height="74" fill="var(--tile-blue)"/>
      <rect x="0" y="148" width="74" height="74" fill="var(--tile-blue)"/>
      <rect x="74" y="148" width="74" height="74" fill="#e6ecef"/>
      <rect x="0" y="222" width="74" height="74" fill="var(--tile-mint)"/>
      <rect x="74" y="222" width="74" height="74" fill="var(--tile-blue)"/>
    </svg>
  </div>
  <div class="loose-piece loose-piece--intro" role="img" aria-label="Puzzle piece cut from the Capitol painting"></div>
</section>

<div class="note note--animation">puzzle animation</div>

<!-- Step 2: pieces flying in -->
<section class="frame frame--assemble">
  <div class="brand brand--solo">CRESTLINE GROUP</div>
  <div class="board">
    <svg width="148" height="296" viewBox="0 0 148 296">
      <rect x="0" y="0" width="74" height="74" fill="var(--tile-blue)"/>
      <rect x="74" y="0" width="74" height="74" fill="var(--tile-mint)"/>
      <rect x="0" y="74" width="74" height="74" fill="var(--tile-mint)"/>
      <rect x="74" y="74" width="74" height="74" fill="var(--tile-blue)"/>
      <rect x="0" y="148" width="74" height="74" fill="var(--tile-blue)"/>
      <rect x="74" y="148" width="74" height="74" fill="#e6ecef"/>
      <rect x="0" y="222" width="74" height="74" fill="var(--tile-mint)"/>
      <rect x="74" y="222" width="74" height="74" fill="var(--tile-blue)"/>
      <rect x="0" y="0" width="74" height="74" fill="url(#painting)" role="img" aria-label="Placed puzzle piece showing the top of the Capitol painting"/>
    </svg>
  </div>
  <div class="loose-piece loose-piece--flying" role="img" aria-label="Rotating puzzle piece with part of the Capitol dome"></div>
</section>

<!-- Step 3: completed painting -->
<section class="frame frame--complete">
  <div class="brand brand--top">CRESTLINE GROUP</div>
  <div class="headline">We Solve<br>Political Puzzle</div>
  <div class="board">
    <svg width="148" height="296" viewBox="0 0 148 296">
      <rect width="148" height="296" fill="url(#painting)" role="img" aria-label="Painting of the Capitol dome in red and gold, cut into puzzle pieces"/>
      <g fill="none" stroke="rgba(255,255,255,0.35)" stroke-width="1.2">
        <line x1="74" y1="0" x2="74" y2="296"/>
        <line x1="0" y1="74" x2="148" y2="74"/>
        <line x1="0" y1="148" x2="148" y2="148"/>
        <line x1="0" y1="222" x2="148" y2="222"/>
      </g>
    </svg>
  </div>
</section>

<div class="note note--buttons">Buttons auto rotation and on rollOver</div>

<!-- Step 4: "Our Clients" button highlighted -->
<section class="frame frame--clients">
  <div class="brand brand--top">CRESTLINE GROUP</div>
  <div class="headline">We Solve<br>Political Puzzle</div>
  <div class="board">
    <svg width="148" height="296" viewBox="0 0 148 296">
      <rect width="148" height="296" fill="url(#painting)" role="img" aria-label="Painting of the Capitol dome in red and gold, cut into puzzle pieces"/>
      <g fill="none" stroke="rgba(255,255,255,0.35)" stroke-width="1.2">
        <line x1="74" y1="0" x2="74" y2="296"/>
        <line x1="0" y1="74" x2="148" y2="74"/>
        <line x1="0" y1="148" x2="148" y2="148"/>
        <line x1="0" y1="222" x2="148" y2="222"/>
      </g>
      <a href="#clients">
        <path d="M0 74 H28 a9 9 0 1 0 18 0 H74 V100 a9 9 0 1 1 0 18 V148 H0 Z" fill="var(--button-navy)"/>
        <text class="button-label" x="37" y="112" text-anchor="middle">Our</text>
        <text class="button-label" x="37" y="125" text-anchor="middle">Clients</text>
      </a>
    </svg>
  </div>
</section>

<!-- Step 5: "Our Team" button highlighted -->
<section class="frame frame--team">
  <div class="brand brand--top">CRESTLINE GROUP</div>
  <div class="headline">We Solve<br>Political Puzzle</div>
  <div class="board">
    <svg width="148" height="296" viewBox="0 0 148 296">
      <rect width="148" height="296" fill="url(#painting)" role="img" aria-label="Painting of the Capitol dome in red and gold, cut into puzzle pieces"/>
      <g fill="none" stroke="rgba(255,255,255,0.35)" stroke-width="1.2">
        <line x1="74" y1="0" x2="74" y2="296"/>
        <line x1="0" y1="74" x2="148" y2="74"/>
        <line x1="0" y1="148" x2="148" y2="148"/>
        <line x1="0" y1="222" x2="148" y2="222"/>
      </g>
      <a href="#team">
        <path d="M74 0 H148 V74 H120 a9 9 0 1 1 -18 0 H74 Z" fill="var(--button-navy)"/>
        <text class="button-label" x="111" y="30" text-anchor="middle">Our</text>
        <text class="button-label" x="111" y="43" text-anchor="middle">Team</text>
      </a>
    </svg>
  </div>
</section>

</body>
</html>
```